Criação de Logo + Papelaria + Manual Básico para Alimentos & Bebidas
" Empresa pequena, ambiental e socialmente responsável, sediada na caatinga baiana, à beira do Rio São Francisco, abastecida por matérias primas de produtores locais. "

```html
<!DOCTYPE html>
<html lang="pt-BR">
<head>
<meta charset="utf-8">
<title>Sertão Raiz — Envelopes</title>
<link rel="stylesheet" href="https://fonts.googleapis.com/css2?family=Alfa+Slab+One&family=Arimo:wght@400&display=swap">
<style>
  :root {
    --backdrop: #f1f1ef;
    --envelope-dark: #262626;
    --envelope-light: #ffffff;
    --leaf-green: #5c9a2e;
    --flap-green: #4f8a26;
    --ink: #2b2b2b;
    --contact-ink: #d8d8d8;
    --shadow: rgba(0, 0, 0, 0.18);
  }
  html, body {
    margin: 0;
    padding: 0;
    width: 1200px;
    height: 1200px;
    overflow: hidden;
    background: var(--backdrop);
  }
  .stationery {
    position: relative;
    width: 1200px;
    height: 1200px;
  }
  .envelope {
    position: absolute;
    overflow: hidden;
    box-shadow: 6px 8px 18px var(--shadow);
  }
  .envelope--back {
    left: 240px;
    top: 320px;
    width: 340px;
    height: 580px;
    background: var(--envelope-dark);
  }
  .envelope--front {
    left: 614px;
    top: 245px;
    width: 346px;
    height: 655px;
    background: var(--envelope-light);
  }
  .flap {
    position: absolute;
    left: 0;
    top: 0;
    width: 100%;
    display: block;
  }
  .brand-lockup {
    position: absolute;
    left: 0;
    right: 0;
    top: 300px;
    text-align: center;
  }
  .brand-mark {
    width: 74px;
    height: 74px;
    margin: 0 auto 14px;
    border-radius: 50%;
    background: var(--leaf-green);
  }
  .brand-name {
    font-family: "Alfa Slab One", serif;
    font-size: 40px;
    letter-spacing: 1px;
    color: var(--ink);
    margin: 0;
    text-transform: uppercase;
  }
  .return-address {
    position: absolute;
    left: 36px;
    top: 500px;
    display: flex;
    align-items: center;
    gap: 18px;
  }
  .return-mark {
    width: 64px;
    height: 64px;
    border-radius: 50%;
    background: var(--leaf-green);
    flex: none;
  }
  .contact-lines {
    font-family: "Arimo", sans-serif;
    font-size: 11px;
    line-height: 15px;
    color: var(--contact-ink);
    margin: 0;
  }
  .contact-lines span { display: block; }
  .social-dot {
    display: inline-block;
    width: 8px;
    height: 8px;
    border-radius: 50%;
    background: var(--contact-ink);
    margin-left: 4px;
    vertical-align: -1px;
  }
</style>
</head>
<body>
<main class="stationery">

  <section class="envelope envelope--back" aria-label="Verso do envelope">
    <svg class="flap" viewBox="0 0 340 110" height="110" aria-hidden="true">
      <polygon points="0,0 340,0 340,40 170,108 0,40" fill="var(--flap-green)"/>
    </svg>
    <div class="return-address">
      <div class="return-mark"></div>
      <p class="contact-lines">
        <span>+ 55 00 0000 - 0000</span>
        <span>Endereço Nome Rua, 0000</span>
        <span>00000 - 000 Bairro / UF - Brasil</span>
        <span>site.com.br <i class="social-dot"></i></span>
      </p>
    </div>
  </section>

  <section class="envelope envelope--front" aria-label="Frente do envelope">
    <svg class="flap" viewBox="0 0 346 50" height="50" aria-hidden="true">
      <path d="M0,0 H346 V30 Q340,48 320,48 H26 Q6,48 0,30 Z" fill="var(--leaf-green)"/>
    </svg>
    <div class="brand-lockup">
      <div class="brand-mark"></div>
      <h1 class="brand-name">Sertão Raiz</h1>
    </div>
  </section>

</main>
</body>
</html>
```